Brivolt VoIP COMMERCIAL PHONE FLYER

We are a full service telecom VoIP company that offers local, long distance calling plans to business clients. We offer local installations, and local service we have a hands on approach and will match or beat any competitor. We work with all types of business. We are fully HIPPA complient in the medical field

Target Market(s)

SMALL TO MEDIUM BUSINESS, Medical, Real Estate, Lawyer, Accounting

Industry/Entity Type

VoIP

Font styles to use
Serif

Colors
0054AA
0677BA
7BADD7
CADEEF
E8F1F8

Requirements
Must have
• Modern/ Current picture of phone reader friendly
Nice to have
• free flow, friendly, modern
Should not have
• stuffy, corporate feel

```html
<!DOCTYPE html>
<html lang="en">
<head>
<meta charset="utf-8">
<title>Brivolt VoIP – Commercial Phone Flyer</title>
<link rel="stylesheet" href="https://fonts.googleapis.com/css2?family=Ubuntu:wght@400;500;700&display=swap">
<style>
  :root{
    --navy:#0a1a33;
    --navy-deep:#061226;
    --brand:#0054AA;
    --brand-mid:#0677BA;
    --sky:#7BADD7;
    --sky-soft:#CADEEF;
    --sky-pale:#E8F1F8;
    --white:#ffffff;
    --page:#e9edf2;
    --ink:#0b1b33;
  }
  *{box-sizing:border-box;margin:0;padding:0}
  html,body{width:1200px;height:800px;overflow:hidden;background:var(--page);font-family:"Ubuntu",sans-serif}
  .stage{position:relative;width:1200px;height:800px}
  .flyer{position:absolute;left:330px;top:20px;width:540px;height:760px;overflow:hidden;
    background:radial-gradient(ellipse at 62% 62%,var(--white) 0%,var(--sky-pale) 30%,var(--sky-soft) 65%,var(--sky) 110%);
    box-shadow:0 10px 30px rgba(10,26,51,.18)}
  .header{position:absolute;inset:0;background:linear-gradient(160deg,var(--navy-deep),var(--navy) 60%,#10284d);
    clip-path:polygon(0 0,100% 0,100% 27%,0 47%)}
  .header-band{position:absolute;left:205px;top:72px;width:335px;height:40px;background:var(--brand-mid)}
  .header-edge{position:absolute;inset:0;background:var(--brand);
    clip-path:polygon(0 47%,100% 27%,100% 28.4%,0 48.4%)}
  .brand-top{position:absolute;left:34px;top:96px;display:flex;align-items:center;gap:10px;
    color:var(--brand-mid);font-weight:700;font-size:36px;letter-spacing:.5px}
  .brand-top .dot,.brand-foot .dot{width:14px;height:14px;border-radius:50%;background:currentColor}
  .headline{position:absolute;left:220px;top:36px;color:var(--white);font-weight:700;text-transform:uppercase;line-height:1;white-space:nowrap}
  .headline span{display:block}
  .headline .l1{font-size:24px;height:36px}
  .headline .l2{font-size:28px;height:40px;line-height:40px;letter-spacing:-.3px}
  .headline .l3{font-size:22px;margin-top:10px}
  .desk-phone{position:absolute;left:80px;top:170px;width:200px;height:240px;border-radius:14px 14px 40px 30px;
    background:linear-gradient(150deg,#3a3f47,#1c1f24 55%,#3b6ea8 56%,#9fc3e6 80%,#2c3036 81%)}
  .cloud-bubble{position:absolute;left:290px;top:180px;width:245px;height:150px}
  .cloud-text{position:absolute;left:322px;top:232px;font-weight:700;line-height:1.05;white-space:nowrap}
  .cloud-text .a{color:var(--brand-mid);font-size:23px;display:block}
  .cloud-text .b{color:var(--ink);font-size:29px;display:block}
  .stat{position:absolute;left:355px;top:325px;width:132px;height:132px;border-radius:50%;
    background:var(--brand);border:6px solid #0d4a8f;display:grid;place-items:center;
    color:var(--white);font-weight:700;font-size:46px}
  .savings{position:absolute;left:34px;top:428px;color:var(--ink);line-height:1;white-space:nowrap}
  .savings .lead{font-size:26px;font-weight:500;display:block}
  .savings .big{font-size:54px;font-weight:700;color:var(--brand);display:block;letter-spacing:-.5px;margin:4px 0}
  .savings .tail{font-size:20px;font-weight:500;display:block}
  .cloud-floor{position:absolute;left:0;bottom:0;width:540px;height:90px}
  .feature{position:absolute;display:flex;flex-direction:column;align-items:center;gap:8px;width:160px}
  .feature .icon{width:72px;height:72px;border-radius:50%;background:var(--brand);display:grid;place-items:center}
  .feature .label{font-weight:700;font-size:16px;color:var(--ink);white-space:nowrap}
  .f-power{left:30px;top:594px}
  .f-use{left:200px;top:556px}
  .f-setup{left:370px;top:490px}
  .brand-foot{position:absolute;left:30px;bottom:16px;display:flex;align-items:center;gap:8px;
    color:var(--brand);font-weight:700;font-size:30px}
  .call{position:absolute;left:190px;bottom:24px}
  .call .kicker{font-size:10px;font-weight:700;color:var(--ink);text-transform:uppercase;display:block;margin-bottom:4px;white-space:nowrap}
  .call .pill{display:inline-flex;align-items:center;gap:8px;background:var(--navy);color:var(--white);
    font-weight:700;font-size:19px;padding:5px 14px;border-radius:20px;white-space:nowrap}
  .web{position:absolute;right:22px;bottom:30px;font-size:12px;font-weight:500;color:var(--ink);white-space:nowrap}
</style>
</head>
<body>
<main class="stage">
  <article class="flyer">
    <div class="header"></div>
    <div class="header-band"></div>
    <div class="header-edge"></div>

    <div class="brand-top"><span class="dot"></span>Brivolt</div>

    <h1 class="headline">
      <span class="l1">We offer free</span>
      <span class="l2">Telephone lines</span>
      <span class="l3">For your business</span>
    </h1>

    <div class="desk-phone" role="img" aria-label="Photo of a modern business desk phone with a touchscreen and corded handset"></div>

    <svg class="cloud-bubble" viewBox="0 0 250 150" aria-hidden="true">
      <path fill="#ffffff" d="M40 140 C10 140 2 110 20 96 C5 78 20 52 45 58 C48 30 80 18 104 34 C120 8 165 8 178 34 C210 24 242 48 232 78 C250 96 238 130 210 130 C200 145 170 148 155 138 C130 150 95 150 80 140 Z"/>
    </svg>
    <p class="cloud-text"><span class="a">Your business</span><span class="b">on the Cloud</span></p>

    <div class="stat">35%</div>

    <p class="savings">
      <span class="lead">We help companies</span>
      <span class="big">SAVE OVER</span>
      <span class="tail">on their monthly phone bills</span>
    </p>

    <svg class="cloud-floor" viewBox="0 0 540 90" preserveAspectRatio="none" aria-hidden="true">
      <path fill="#eef5fb" d="M0 40 C40 18 90 24 110 40 C140 14 200 18 215 36 C250 18 300 22 320 36 C350 8 420 8 440 28 C470 12 520 15 540 26 L540 90 L0 90 Z"/>
      <path fill="#ffffff" d="M0 58 C50 42 100 48 130 58 C170 44 230 44 260 58 C300 44 360 44 390 56 C430 42 500 42 540 52 L540 90 L0 90 Z"/>
    </svg>

    <div class="feature f-setup">
      <div class="icon">
        <svg width="40" height="40" viewBox="0 0 44 44" aria-hidden="true">
          <circle cx="22" cy="22" r="11" fill="none" stroke="#fff" stroke-width="4" stroke-dasharray="5 3"/>
          <circle cx="22" cy="22" r="5" fill="none" stroke="#fff" stroke-width="3"/>
        </svg>
      </div>
      <span class="label">Easy set up</span>
    </div>

    <div class="feature f-use">
      <div class="icon">
        <svg width="36" height="36" viewBox="0 0 40 40" aria-hidden="true">
          <path d="M12 6 L12 32 L18 26 L23 36 L27 34 L22 24 L30 24 Z" fill="#fff"/>
        </svg>
      </div>
      <span class="label">Easy to use</span>
    </div>

    <div class="feature f-power">
      <div class="icon">
        <svg width="36" height="36" viewBox="0 0 40 40" aria-hidden="true">
          <path d="M23 4 L10 23 L19 23 L16 36 L30 16 L21 16 Z" fill="#fff"/>
        </svg>
      </div>
      <span class="label">Powerful features</span>
    </div>

    <div class="brand-foot"><span class="dot"></span>Brivolt</div>

    <div class="call">
      <span class="kicker">Call today for your free phones</span>
      <span class="pill">
        <svg width="14" height="14" viewBox="0 0 24 24" aria-hidden="true">
          <path fill="#7BADD7" d="M6.6 10.8a15 15 0 0 0 6.6 6.6l2.2-2.2c.3-.3.7-.4 1-.2 1.1.4 2.3.6 3.6.6.6 0 1 .4 1 1V20c0 .6-.4 1-1 1A17 17 0 0 1 3 4c0-.6.4-1 1-1h3.5c.6 0 1 .4 1 1 0 1.3.2 2.5.6 3.6.1.3 0 .7-.2 1z"/>
        </svg>
        555-014-2290
      </span>
    </div>

    <p class="web">www.brivoltvoice.net</p>
  </article>
</main>
</body>
</html>
```